Business Card

I need a business card for my work as an energy lawyer. I am a single prctioner and I consult to energy companies regarding a variety of legal issues involving environmental matters, energy efficiency, regulations and contractual arrangements. i need a distinctive business card that stands out and is easy to read. I like bold colors or high contrast. I like a sparse architectural design. The font should be easy to read (many of my clients use reading glasses and are concerned about small type). The card should communicate that I am somewhat different from ordinary legal counsel. Below are some examples of cards that I like. Thank you for your interest and thought. Glenn Dusty Harker
Updates

Thanks to everyone who has submitted a design.  My general comments are:

1.  I like the colourful cards and the high contrast cards.
2.  I prefer the use of icons for home address, phone, mobile and email.
3.  For the high contrast cards please use three colours - black background, and red and white for the logo or information.
4.  The mobile number area code should be 403 and not 404.
5.  I also need to add a direct phone line which is 403-517-6392.

Thank you,

Glenn Harker

Reason: I have briefly extended the deadline by three days to allow those individuals who responded early to revise their designs based upon the subsequent clarification of the colours (red, white, black background) and the request to use icons and add a direct phone number.

Industry/Entity Type

Business

```html
<!DOCTYPE html>
<html lang="en">
<head>
<meta charset="utf-8">
<title>Glenn Dusty Harker — Business Card</title>
<link rel="stylesheet" href="https://fonts.googleapis.com/css2?family=Comfortaa:wght@400;700&display=swap">
<style>
  :root {
    --orange: #f39a2e;
    --orange-deep: #ee8a1c;
    --ink: #1c1c1c;
    --paper: #ffffff;
    --backdrop: #ece8e2;
    --card-radius: 16px;
  }
  * { margin: 0; padding: 0; box-sizing: border-box; }
  html, body {
    width: 1200px;
    height: 1023px;
    overflow: hidden;
  }
  body {
    background: var(--backdrop);
    font-family: "Comfortaa", "Trebuchet MS", sans-serif;
    display: flex;
    flex-direction: column;
    align-items: center;
    justify-content: center;
    gap: 60px;
  }
  .card {
    width: 600px;
    height: 343px;
    border-radius: var(--card-radius);
    box-shadow: 0 6px 18px rgba(0, 0, 0, 0.15);
    position: relative;
    overflow: hidden;
  }

  /* Front */
  .card-front {
    background: var(--orange);
    color: var(--paper);
    display: flex;
    flex-direction: column;
    justify-content: center;
    padding: 0 40px 20px;
  }
  .card-front .name {
    font-weight: 700;
    font-size: 44px;
    line-height: 1.15;
  }
  .card-front .title {
    font-weight: 400;
    font-size: 25px;
    margin-top: 6px;
  }

  /* Back */
  .card-back {
    background: var(--paper);
    padding: 30px 40px 0 34px;
  }
  .card-back .name {
    color: var(--orange);
    font-weight: 700;
    font-size: 40px;
    line-height: 1.1;
  }
  .card-back .title {
    color: var(--ink);
    font-weight: 400;
    font-size: 23px;
    margin-top: 4px;
    padding-bottom: 10px;
    border-bottom: 2px solid var(--orange);
  }
  .address {
    display: flex;
    align-items: center;
    gap: 10px;
    color: var(--orange);
    font-size: 19px;
    margin-top: 18px;
  }
  .contact-list {
    margin-top: 12px;
    display: grid;
    grid-template-columns: 30px 84px 22px auto;
    align-items: center;
    row-gap: 6px;
    font-size: 17px;
  }
  .icon {
    width: 20px;
    height: 20px;
    fill: none;
    stroke: var(--orange-deep);
    stroke-width: 2;
    stroke-linecap: round;
    stroke-linejoin: round;
    flex: none;
  }
  .contact-list .label,
  .contact-list .sep {
    color: var(--orange-deep);
    font-weight: 700;
  }
  .contact-list .value {
    color: var(--ink);
    font-weight: 700;
  }
</style>
</head>
<body>
  <section class="card card-front" aria-label="Business card front">
    <h1 class="name">Glenn Dusty Harker</h1>
    <p class="title">Barrister &amp; Solicitor, LLB, ICD.D</p>
  </section>

  <section class="card card-back" aria-label="Business card back">
    <h2 class="name">Glenn Dusty Harker</h2>
    <p class="title">Barrister &amp; Solicitor, LLB, ICD.D</p>
    <p class="address">
      <svg class="icon" viewBox="0 0 24 24" aria-hidden="true"><path d="M12 22s-7-7.5-7-13a7 7 0 0 1 14 0c0 5.5-7 13-7 13z"/><circle cx="12" cy="9" r="2.5"/></svg>
      2740 9th Avenue S.W., Calgary, Alberta
    </p>
    <div class="contact-list">
      <svg class="icon" viewBox="0 0 24 24" aria-hidden="true"><path d="M5 3h4l2 5-2.5 1.5a11 11 0 0 0 6 6L16 13l5 2v4a2 2 0 0 1-2 2A17 17 0 0 1 3 5a2 2 0 0 1 2-2z"/></svg>
      <span class="label">Phone</span><span class="sep">:</span><span class="value">1.403.628.1945</span>

      <svg class="icon" viewBox="0 0 24 24" aria-hidden="true"><path d="M5 3h4l2 5-2.5 1.5a11 11 0 0 0 6 6L16 13l5 2v4a2 2 0 0 1-2 2A17 17 0 0 1 3 5a2 2 0 0 1 2-2z"/><path d="M15 3a6 6 0 0 1 6 6"/></svg>
      <span class="label">Direct</span><span class="sep">:</span><span class="value">1.403.517.6392</span>

      <svg class="icon" viewBox="0 0 24 24" aria-hidden="true"><rect x="7" y="2" width="10" height="20" rx="2"/><path d="M11 18h2"/></svg>
      <span class="label">Mobile</span><span class="sep">:</span><span class="value">1.403.382.9016</span>

      <svg class="icon" viewBox="0 0 24 24" aria-hidden="true"><rect x="3" y="5" width="18" height="14" rx="2"/><path d="M3 7l9 6 9-6"/></svg>
      <span class="label">Email</span><span class="sep">:</span><span class="value">dusty@dustyharker.com</span>
    </div>
  </section>
</body>
</html>
```